Label Sticker for Tea Bag and Herbs and Spices Bag

I want to design the product label sticker size in 60 mm (H) x 100 mm (W).
This label is for our product herbal tea bag. We sell herbs such as Rose buds, Lavender, Chamomile, etc they are consider flower tea. Our products are natural dry herbs and spices.
I select Green, Brown, white as color combination. I can accept other colour proposed. If it look nice. However, only maximum 3 colours to play around and white is a compulsory colour.
I will print the product name, description, expiry date and instruction how to use and company name and address on it in black ink.
Prefer the label have natural look.
I would like to place my company logo in the label. Attached is the full colour artwork logo file.
I can accept one colour for logo since I only use 3 maximum colour.

Please advise the best design.

Reason: I am sorry as first time use Tally orchard, I am not sure how to use the system.

Target Market(s)

To consumer who drink tea

Industry/Entity Type

It Company

Font styles to use
Serif

Requirements
Must have
• 60 mm (H) x 100 mm (w)
• Maximum 3 colour to play.
• Natural look and attraction to consumers.
Nice to have
• -Some drawing such as flower or leaves, lines, waves... as wallpaper
• -Can use 3 colour to separate Products name, Description and How to use.
• -Can give different colour besides my request for comparison.
• -Nice frame
Should not have
• Big pictures - Because it take the spaces, I cannot write more information in the label
• Too dark colour -Consumer cannot see the product information very clearly
• Too big logo - As it will take the space of the label.

```html
<!DOCTYPE html>
<html lang="en">
<head>
<meta charset="utf-8">
<title>Meadow Steep – Product Label</title>
<link rel="stylesheet" href="https://fonts.googleapis.com/css2?family=Jost:wght@400&family=Marcellus+SC&display=swap">
<style>
  :root {
    --paper: #ffffff;
    --leaf-wash: #eef6cc;
    --leaf-green: #a9d00f;
    --gold: #c9a030;
    --ochre: #c7923a;
    --terracotta: #cd4f45;
    --ink: #111111;
  }
  * { box-sizing: border-box; margin: 0; padding: 0; }
  html, body {
    width: 1200px;
    height: 720px;
    overflow: hidden;
    background: var(--paper);
  }
  .label {
    position: relative;
    width: 1200px;
    height: 720px;
    background: var(--paper);
    font-family: "Jost", "Helvetica Neue", Arial, sans-serif;
    font-weight: 400;
    color: var(--ink);
    overflow: hidden;
  }
  .label__wash {
    position: absolute;
    left: 0;
    top: 0;
    width: 700px;
    height: 720px;
  }
  .centered {
    position: absolute;
    left: 0;
    width: 1200px;
    text-align: center;
    font-weight: 400;
  }
  .brand {
    top: 180px;
    display: flex;
    justify-content: center;
    align-items: center;
    gap: 16px;
  }
  .brand__dot {
    width: 22px;
    height: 22px;
    border-radius: 50%;
    background: var(--leaf-green);
  }
  .brand__name {
    font-family: "Jost", "Helvetica Neue", Arial, sans-serif;
    font-weight: 400;
    font-size: 58px;
    line-height: 1;
    letter-spacing: 2px;
    color: var(--gold);
    text-transform: uppercase;
  }
  .product-name {
    top: 312px;
    font-family: "Marcellus SC", Georgia, serif;
    font-size: 36px;
    line-height: 44px;
    letter-spacing: 1px;
    text-transform: uppercase;
    color: var(--terracotta);
    display: flex;
    justify-content: center;
    align-items: center;
    gap: 16px;
  }
  .product-name__dot {
    width: 13px;
    height: 13px;
    border-radius: 50%;
    background: var(--leaf-green);
  }
  .descriptor {
    top: 372px;
    font-family: "Marcellus SC", Georgia, serif;
    font-size: 23px;
    line-height: 28px;
    letter-spacing: 1.5px;
    text-transform: uppercase;
    color: var(--ochre);
  }
  .instructions__title {
    top: 432px;
    font-size: 20px;
    line-height: 26px;
    color: var(--leaf-green);
  }
  .instructions__body {
    top: 458px;
    left: 320px;
    width: 560px;
    font-size: 19.5px;
    line-height: 26px;
    color: var(--ink);
  }
  .best-before {
    top: 567px;
    font-size: 11px;
    color: var(--ink);
  }
  .address {
    top: 604px;
    font-size: 20.5px;
    color: var(--ink);
    display: flex;
    justify-content: center;
    align-items: center;
    gap: 13px;
  }
  .address__dot {
    width: 6px;
    height: 6px;
    border-radius: 50%;
    background: var(--leaf-green);
  }
  .website {
    top: 633px;
    left: -34px;
    font-size: 19px;
    letter-spacing: 7px;
    color: var(--ink);
  }
</style>
</head>
<body>
  <main class="label">
    <svg class="label__wash" viewBox="0 0 700 720" role="img" aria-label="Faint pale green leaf decoration in the background">
      <defs>
        <radialGradient id="wash" cx="0.4" cy="0.5" r="0.6">
          <stop offset="0" stop-color="#eef6cc" stop-opacity="0.95"/>
          <stop offset="0.7" stop-color="#eef6cc" stop-opacity="0.55"/>
          <stop offset="1" stop-color="#ffffff" stop-opacity="0"/>
        </radialGradient>
      </defs>
      <rect width="700" height="720" fill="url(#wash)"/>
    </svg>

    <div class="centered brand">
      <span class="brand__dot"></span>
      <span class="brand__name">Meadow Steep</span>
    </div>

    <h1 class="centered product-name">
      <span class="product-name__dot"></span>Product Name<span class="product-name__dot"></span>
    </h1>
    <p class="centered descriptor">A skin softening herbal tea product</p>

    <h2 class="centered instructions__title">How to apply:</h2>
    <p class="centered instructions__body">Lorem ipsum dolor sit amet, consectetur adipisicing elit, sed do eiusmod tempor incididunt ut labore et dolore magna aliqua. Ut enim ad minim veniam, quis nostrud exullamco</p>

    <p class="centered best-before">Best until March 28, 2020</p>

    <p class="centered address">
      <span>Meadow Steep</span><span class="address__dot"></span>
      <span>1234 Main Street</span><span class="address__dot"></span>
      <span>City, State 12345</span>
    </p>
    <p class="centered website">www.yourwebsite.com</p>
  </main>
</body>
</html>
```